Healthy Vending Machine Business Flyer

A modorn design that represents our healthy vending machine business. We will attach a picture of the machine we want on the flyer along with our logo. We will also upload the wording we want on the flyer

Colors

Designer to choose colors to be used in the design.

Requirements
Must have
• Flyer wording
• Front of flyer:
• (Picture of vending machine on the front)
• Free healthy vending machines hit the Treasure Valley
• Keep your Employees happy & productive with healthy vending options at work
• • No Cost to Your Company
• • Remote tracking tells us when your favorite snacks are running low
• • Credit Card/Smartphone Payment Technology
• • Ability to Customize your Snacks and Drinks
• • Locally Owned and Operated
• • Delicious Healthy Options
• Back of flyer:
• Quillow Healthy Vending is a locally owned and operated company dedicated to making healthy snacks and drinks easily available for the Treasure Valley. We provide the latest in vending machine technology accepting credit cards, zenno pay, and nimbus wallet. State of the art inventory tracking tells us when your machine is running low so you're never out of your favorite drink or snack. We offer flexible stocking based on your companies needs and work with you on what items you want in the machine. Our goal is to give your employees and clients healthy options on the go
• To be considered for this FREE service for your business please visit: quillowhealthyvending.com
• Or call/email today:
• Phone: 555-201-4736
• Email: quillowhealthyvending@mailvex.com
Should not have
• Any Additional Fruit images besides what is on the machine image.

```html
<!DOCTYPE html>
<html lang="en">
<head>
<meta charset="utf-8">
<title>Quillow Healthy Vending – Flyer Front and Back</title>
<link href="https://fonts.googleapis.com/css2?family=Ubuntu:wght@700&family=Source+Sans+3:wght@300;400;600;700&family=Roboto+Condensed:wght@700&display=swap" rel="stylesheet">
<style>
  :root{
    --board:#2b2b2d;
    --paper:#f7f7f7;
    --green:#3a8f3e;
    --green-bright:#5aa83a;
    --orange:#f07a1a;
    --yellow:#fcc614;
    --yellow-deep:#f9a91a;
    --ink:#1e1e1e;
    --brown:#3a2a0a;
    --white:#ffffff;
  }
  *{margin:0;padding:0;box-sizing:border-box}
  html,body{width:1200px;height:889px;overflow:hidden;background:var(--board)}
  .board{position:relative;width:1200px;height:889px;background:var(--board)}
  .flyer{position:absolute;top:107px;width:471px;height:666px;overflow:hidden;box-shadow:4px 6px 10px rgba(0,0,0,.55)}
  .flyer--back{left:124px;background:radial-gradient(ellipse at 30% 25%,#ffffff 0%,#f1f1f1 45%,#e4e4e4 100%)}
  .flyer--front{left:623px;background:radial-gradient(circle at 45% 55%,#ffd21c 0%,var(--yellow) 45%,var(--yellow-deep) 100%)}
  .abs{position:absolute}

  /* back */
  .back-title{left:31px;top:26px;font:700 26px/33px 'Ubuntu',sans-serif;color:var(--green);letter-spacing:-.2px}
  .machine-photo{background:linear-gradient(160deg,#2a2a2a 0%,#3d6b25 30%,#b3261e 60%,#2b2b2b 100%)}
  .back-machine{left:30px;top:138px;width:148px;height:275px}
  .back-intro{left:203px;top:150px;width:244px;font:300 13px/16.8px 'Source Sans 3',sans-serif;color:var(--green)}
  .back-cta{left:203px;top:412px;width:244px;font:400 13px/16px 'Source Sans 3',sans-serif;color:var(--ink)}
  .back-email{left:203px;top:449px;font:700 12px/16px 'Source Sans 3',sans-serif;color:var(--orange);letter-spacing:.2px}
  .back-site{left:203px;top:480px;font:700 18px/22px 'Source Sans 3',sans-serif;color:var(--green);letter-spacing:.3px}
  .back-brand{left:206px;top:560px;width:230px;font:700 26px/28px 'Source Sans 3',sans-serif;color:var(--orange)}
  .back-tagline{left:40px;top:445px;width:124px;text-align:center;font:300 16px/22.5px 'Source Sans 3',sans-serif;color:var(--ink)}
  .social{left:64px;top:549px;display:flex;gap:11px}
  .social span{width:33px;height:33px;border-radius:50%;background:var(--green)}
  .back-call{left:0;width:210px;top:603px;text-align:center;font:700 14px/18px 'Source Sans 3',sans-serif;color:var(--orange)}
  .back-phone{left:0;width:210px;top:620px;text-align:center;font:700 27px/32px 'Roboto Condensed',sans-serif;color:var(--green)}

  /* front */
  .front-title{left:37px;top:26px;font:700 33px/43px 'Ubuntu',sans-serif;color:var(--white);text-shadow:2px 2px 3px rgba(120,60,0,.55)}
  .front-machine{left:23px;top:179px;width:215px;height:401px}
  .badge{left:256px;top:148px;width:180px;height:180px;border-radius:50%;background:radial-gradient(circle at 45% 35%,#ffffff 0%,#f3f3f3 70%,#d9d9d9 100%);box-shadow:0 4px 8px rgba(120,60,0,.45);text-align:center}
  .badge-brand{position:absolute;left:14px;right:14px;top:46px;font:700 17px/19px 'Source Sans 3',sans-serif;color:var(--orange)}
  .badge-note{position:absolute;left:18px;right:18px;top:118px;font:400 10.5px/13.5px 'Source Sans 3',sans-serif;color:var(--ink)}
  .front-pitch{left:264px;top:343px;width:200px;font:300 19px/23px 'Source Sans 3',sans-serif;color:var(--brown)}
  .benefits{left:264px;top:456px;width:200px;list-style:none}
  .benefits li{position:relative;padding-left:15px;margin-bottom:6px;font:600 11px/13px 'Source Sans 3',sans-serif;color:var(--brown)}
  .benefits li::before{content:"";position:absolute;left:0;top:2px;width:9px;height:9px;border-radius:50%;background:radial-gradient(circle at 35% 35%,#b6e27a,var(--green-bright))}
  .front-site{left:46px;top:588px;font:700 15px/18px 'Source Sans 3',sans-serif;color:var(--white);letter-spacing:.4px;text-shadow:1px 1px 2px rgba(120,60,0,.6)}
  .front-band{left:0;top:600px;width:471px;height:66px}
  .front-contact{left:51px;top:638px;font:700 15px/18px 'Roboto Condensed',sans-serif;color:var(--white)}
  .front-contact em{font-size:11px;font-style:normal}
</style>
</head>
<body>
<main class="board">

  <section class="flyer flyer--back" aria-label="Flyer back">
    <h1 class="abs back-title">Free healthy Vending Machines<br>hit the Treasure Valley</h1>
    <div class="abs machine-photo back-machine" role="img" aria-label="Photo of the healthy vending machine with fruit wrap"></div>
    <p class="abs back-intro">Quillow Healthy Vending is a locally owned and operated company dedicated to making healthy snacks and drinks easily available for the Treasure Valley. We provide the latest in vending machine technology accepting credit cards, zenno pay, and nimbus wallet. State of the art inventory tracking tells us when your machine is running low so you’re never out of your favorite drink or snack. We offer flexible stocking based on your companies needs and work with you on what items you want in the machine. Our goal is to give your employees and clients healthy options on the go</p>
    <p class="abs back-cta">To be considered for this FREE service for your business please visit or email</p>
    <p class="abs back-email">quillowhealthyvending@mailvex.com</p>
    <p class="abs back-site">quillowhealthyvending.com</p>
    <p class="abs back-brand">Quillow Healthy Vending</p>
    <p class="abs back-tagline">Healthy vending options are now available in your area</p>
    <div class="abs social" aria-label="Social media links"><span></span><span></span></div>
    <p class="abs back-call">call/email today:</p>
    <p class="abs back-phone">555-201-4736</p>
  </section>

  <section class="flyer flyer--front" aria-label="Flyer front">
    <h1 class="abs front-title">Free healthy Vending<br>Machines hit the<br>Treasure Valley</h1>
    <div class="abs machine-photo front-machine" role="img" aria-label="Photo of the healthy vending machine with fruit wrap"></div>
    <div class="abs badge">
      <p class="badge-brand">Quillow Healthy Vending</p>
      <p class="badge-note">To be considered for this FREE service for your business please visit our site</p>
    </div>
    <p class="abs front-pitch">Keep your Employees happy &amp; productive with healthy vending options at work</p>
    <ul class="abs benefits">
      <li>No Cost to Your Company</li>
      <li>Remote tracking tells us when your favorite snacks are running low</li>
      <li>Credit Card/Smartphone Payment Technology</li>
      <li>Ability to Customize your Snacks and Drinks</li>
      <li>Locally Owned and Operated</li>
      <li>Delicious Healthy Options</li>
    </ul>
    <p class="abs front-site">quillowhealthyvending.com</p>
    <svg class="abs front-band" viewBox="0 0 471 66" aria-hidden="true">
      <path d="M0 36 C120 14 300 10 471 6 L471 66 L0 66 Z" fill="#f5a020"/>
      <path d="M0 42 C140 20 330 22 471 12 L471 66 L0 66 Z" fill="#ef6f1a"/>
      <path d="M0 48 C150 30 340 36 471 24 L471 66 L0 66 Z" fill="#6fb13a"/>
    </svg>
    <p class="abs front-contact"><em>Contact us : </em>555-201-4736</p>
  </section>

</main>
</body>
</html>
```